Copper Tide E-Liquid - We need four labels designed and a logo.

We need four labels designed for our eliquid line.
The labels should have some artwork showing the flavors of each of the liquids. The list below shows what they are. Also, we would like some type of logo design, that will keep the labels uniform.
Biscuit Hoops - a cinnamon toast cereal
Orange mango kiwi - Orange, mango, and kiwi.
Pink Fizzle - Pink Fizzle
Zelo Berry - Fiji apple, watermelon, and guava.

Logo Text

Copper Tide

Requirements
Must have
• The project must have the overlay I just uploaded.

```html
<!DOCTYPE html>
<html lang="en">
<head>
<meta charset="utf-8">
<title>Copper Tide E-Liquid – Biscuit Hoops Label</title>
<link rel="stylesheet" href="https://fonts.googleapis.com/css2?family=Montserrat:wght@500;600&display=swap">
<style>
  :root {
    --backdrop: #e9edf1;
    --label-white: #ffffff;
    --copper: #ec9a55;
    --copper-deep: #d9773a;
    --band-copper: #eea061;
    --streak-grey: #eef0f2;
  }
  html, body {
    margin: 0;
    padding: 0;
    width: 1200px;
    height: 900px;
    overflow: hidden;
    background: var(--backdrop);
  }
  .canvas {
    position: relative;
    width: 1200px;
    height: 900px;
    display: flex;
    align-items: center;
    justify-content: center;
  }
  .label {
    position: relative;
    width: 620px;
    height: 716px;
    background: var(--label-white);
    font-family: "Montserrat", sans-serif;
    box-shadow: 0 2px 10px rgba(60, 80, 100, 0.08);
  }
  .brand-name {
    position: absolute;
    top: 78px;
    left: 0;
    right: 0;
    margin: 0;
    text-align: center;
    font-weight: 600;
    font-size: 58px;
    letter-spacing: -0.5px;
    color: var(--copper);
  }
  .speed-streaks {
    position: absolute;
    top: 200px;
    left: 0;
    width: 620px;
    height: 300px;
  }
  .brand-mark {
    position: absolute;
    top: 255px;
    left: 230px;
    width: 160px;
    height: 160px;
    border-radius: 50%;
    background: var(--copper-deep);
  }
  .flavour-band {
    position: absolute;
    top: 536px;
    left: 0;
    right: 0;
    height: 56px;
    background: var(--band-copper);
    display: flex;
    align-items: center;
    justify-content: center;
  }
  .flavour-name {
    margin: 0;
    font-weight: 500;
    font-size: 24px;
    letter-spacing: -0.5px;
    color: var(--label-white);
    text-transform: uppercase;
  }
  .spec-row {
    position: absolute;
    top: 614px;
    left: 0;
    right: 0;
    display: flex;
    justify-content: center;
    gap: 130px;
    font-weight: 500;
    font-size: 24px;
    color: var(--copper);
  }
</style>
</head>
<body>
  <main class="canvas">
    <section class="label">
      <h1 class="brand-name">COPPER TIDE</h1>
      <svg class="speed-streaks" viewBox="0 0 620 300" aria-hidden="true">
        <g stroke="var(--streak-grey)" stroke-width="14" stroke-linecap="round">
          <line x1="20" y1="40" x2="160" y2="40"/>
          <line x1="40" y1="80" x2="120" y2="80"/>
          <line x1="460" y1="40" x2="600" y2="40"/>
          <line x1="480" y1="90" x2="560" y2="90"/>
          <line x1="440" y1="140" x2="590" y2="140"/>
          <line x1="470" y1="190" x2="580" y2="190"/>
          <line x1="400" y1="240" x2="470" y2="240"/>
        </g>
      </svg>
      <div class="brand-mark" aria-hidden="true"></div>
      <div class="flavour-band">
        <p class="flavour-name">Biscuit Hoops</p>
      </div>
      <div class="spec-row">
        <span class="spec-strength">03 mg</span>
        <span class="spec-volume">30 ml</span>
      </div>
    </section>
  </main>
</body>
</html>
```